Surgery Office Letterhead Design

I'm seeking new letterhead that will comprise all of our office locations and logo and other applicable information, per the following:

Office Locations:

Lakemont Institute for Jaw & Face Surgery at Cleburne
347 Hazelpine Court
Cleburne, Texas 76091
Phone 817.382.4706
Fax 817.382.9034

Lakemont Institute for Jaw & Face Surgery at Stephenville
518 Willowgate Boulevard
Stephenville, Texas 76458
Phone 254.563.2781
Fax 254.563.2789

Lakemont Institute for Jaw & Face Surgery at Belton
739 West 9th Avenue
Belton, Texas 76582
Phone 254.871.4035
Fax 254.871.4042

Other Info to include:

www.lakemontjawface.com
hello@lakemontjawface.com

Industry/Entity Type

Medical

Font styles to use
Serif
Sans Serif

Requirements
Must have
• See Project Description

```html
<!DOCTYPE html>
<html lang="en">
<head>
<meta charset="utf-8">
<title>Lakemont Institute for Jaw &amp; Face Surgery — Letterhead</title>
<link rel="stylesheet" href="https://fonts.googleapis.com/css2?family=Arimo:wght@400&family=Cormorant+Garamond:wght@600&display=swap">
<style>
  :root {
    --brand-blue: #0f3399;
    --brand-mint: #6cdfb3;
    --contact-blue: #1f22e6;
    --mark-ink: #1c1c24;
    --paper: #ffffff;
  }
  html, body {
    margin: 0;
    padding: 0;
    overflow: hidden;
    background: var(--paper);
  }
  .letterhead {
    position: relative;
    width: 927px;
    height: 1200px;
    overflow: hidden;
    background: var(--paper);
    font-family: "Arimo", Arial, sans-serif;
  }
  .band {
    position: absolute;
    left: 0;
    top: 0;
    width: 927px;
    height: 72px;
  }
  .band span { position: absolute; display: block; }
  .band .strip-top-left { left: 0; top: 0; width: 761px; height: 27px; background: var(--brand-mint); }
  .band .strip-top-right { left: 761px; top: 0; width: 166px; height: 27px; background: var(--brand-blue); }
  .band .strip-bottom-left { left: 0; top: 27px; width: 761px; height: 45px; background: var(--brand-blue); }
  .band .strip-bottom-right { left: 761px; top: 27px; width: 166px; height: 45px; background: var(--brand-mint); }

  .brand {
    position: absolute;
    left: 55px;
    top: 110px;
    display: flex;
    align-items: center;
    gap: 10px;
  }
  .brand-square {
    width: 26px;
    height: 26px;
    background: var(--brand-blue);
    flex: none;
  }
  .brand-name {
    margin: 0;
    font-family: "Cormorant Garamond", Georgia, serif;
    font-weight: 600;
    font-size: 21px;
    line-height: 22px;
    color: var(--mark-ink);
  }
  .brand-links {
    position: absolute;
    left: 115px;
    top: 174px;
    font-size: 10.5px;
    line-height: 13px;
    color: var(--contact-blue);
  }
  .brand-links a { color: inherit; text-decoration: none; display: block; }

  .office {
    position: absolute;
    top: 107px;
    margin: 0;
    font-style: normal;
    font-size: 10.2px;
    line-height: 12.7px;
    color: var(--contact-blue);
    white-space: nowrap;
    letter-spacing: -0.15px;
  }
  .office--cleburne { left: 315px; }
  .office--stephenville { left: 513px; }
  .office--belton { left: 711px; }
  .office span { display: block; }
</style>
</head>
<body>
<main class="letterhead">
  <div class="band" aria-hidden="true">
    <span class="strip-top-left"></span>
    <span class="strip-top-right"></span>
    <span class="strip-bottom-left"></span>
    <span class="strip-bottom-right"></span>
  </div>

  <header class="brand">
    <span class="brand-square" aria-hidden="true"></span>
    <p class="brand-name">Lakemont Institute<br>for Jaw &amp; Face Surgery</p>
  </header>
  <div class="brand-links">
    <a href="#">www.lakemontjawface.com</a>
    <a href="#">hello@lakemontjawface.com</a>
  </div>

  <address class="office office--cleburne">
    <span>Lakemont Institute for Jaw &amp; Face Surgery</span>
    <span>at Cleburne</span>
    <span>347 Hazelpine Court</span>
    <span>Cleburne, Texas 76091</span>
    <span>Phone 817.382.4706</span>
    <span>Fax 817.382.9034</span>
  </address>

  <address class="office office--stephenville">
    <span>Lakemont Institute for Jaw &amp; Face Surgery</span>
    <span>at Stephenville</span>
    <span>518 Willowgate Boulevard</span>
    <span>Stephenville, Texas 76458</span>
    <span>Phone 254.563.2781</span>
    <span>Fax 254.563.2789</span>
  </address>

  <address class="office office--belton">
    <span>Lakemont Institute for Jaw &amp; Face Surgery</span>
    <span>at Belton</span>
    <span>739 West 9th Avenue</span>
    <span>Belton, Texas 76582</span>
    <span>Phone 254.871.4035</span>
    <span>Fax 254.871.4042</span>
  </address>
</main>
</body>
</html>
```